Harbor Ledger BC

I have a baseline business card that I would like to spruce up!

I actually like this business card. I just want to find a way to have all the information below on it and it too look balanced and professional.

Target Market(s)

Small to medium sized companies - Health Insurance Consulting

Industry/Entity Type

Health Insurance

Contact Information for Business Card

The information I would like included on the business card is:

- Harbor Ledger Pacific Title and logo
- Dana Whitlow
- Business title: Principal
- 4312 Alder Crest Rd Suite C-215 Fernvale, WA 98172
- Employee Benefits Consulting & (Wellness Consulting) optional
- dana@harborledgerpac.com
- cell: 425-731-4062

Font styles to use
Other font styles liked:
• I like the font it is currently in but am open to others.

Requirements
Must have
• I like the logo and the color scheme. I even like the layout. I just need to fine tune it!

```html
<!DOCTYPE html>
<html lang="en">
<head>
<meta charset="utf-8">
<title>Harbor Ledger Pacific – Business Card</title>
<link rel="stylesheet" href="https://fonts.googleapis.com/css2?family=Lato:wght@400;700&display=swap">
<style>
  :root {
    --brand-green: #2b6e3d;
    --text-grey: #a9a9a9;
    --rule-grey: #dcdcdc;
    --card-white: #ffffff;
    --page-bg: #e9e7e3;
  }
  html, body {
    margin: 0;
    width: 1200px;
    height: 902px;
    overflow: hidden;
    background: var(--page-bg);
    font-family: "Lato", Arial, sans-serif;
  }
  .business-card {
    position: absolute;
    left: 100px;
    top: 165px;
    width: 1000px;
    height: 571px;
    background: var(--card-white);
    overflow: hidden;
    box-shadow: 0 6px 24px rgba(0,0,0,0.12);
  }
  .brand-mark {
    position: absolute;
    left: 51px;
    top: 72px;
    width: 106px;
    height: 106px;
    border-radius: 50%;
    background: var(--brand-green);
  }
  .brand-name {
    position: absolute;
    left: 178px;
    top: 92px;
    width: 374px;
    text-align: right;
    color: var(--text-grey);
    font-weight: 400;
    line-height: 1;
  }
  .brand-name .line-main { display: block; font-size: 41px; letter-spacing: 0.5px; }
  .brand-name .line-sub { display: block; font-size: 26px; margin-top: 4px; letter-spacing: 0.5px; }
  .brand-divider {
    position: absolute;
    left: 580px;
    top: 60px;
    width: 1px;
    height: 143px;
    background: var(--rule-grey);
  }
  .service-tagline {
    position: absolute;
    left: 602px;
    top: 86px;
    margin: 0;
    color: var(--text-grey);
    font-size: 23px;
    line-height: 28px;
  }
  .brand-pattern {
    position: absolute;
    left: 660px;
    top: 40px;
    width: 560px;
    height: 560px;
    border-radius: 50%;
    background: var(--brand-green);
  }
  .contact-person {
    position: absolute;
    left: 51px;
    top: 252px;
  }
  .person-name {
    margin: 0;
    color: var(--text-grey);
    font-size: 32px;
    font-weight: 400;
    line-height: 36px;
  }
  .person-title {
    margin: 0;
    color: var(--brand-green);
    font-size: 26px;
    font-weight: 700;
    line-height: 32px;
  }
  .postal-address {
    position: absolute;
    left: 51px;
    top: 354px;
    font-style: normal;
    color: var(--text-grey);
    font-size: 25px;
    line-height: 33px;
  }
  .contact-list {
    position: absolute;
    left: 51px;
    top: 448px;
    margin: 0;
    padding: 0;
    list-style: none;
    color: var(--text-grey);
    font-size: 25px;
  }
  .contact-list li {
    display: flex;
    align-items: center;
    height: 42px;
  }
  .contact-icon {
    width: 32px;
    height: 32px;
    margin-right: 14px;
    flex: none;
  }
</style>
</head>
<body>
  <section class="business-card">
    <div class="brand-mark" aria-hidden="true"></div>
    <div class="brand-name">
      <span class="line-main">HARBOR LEDGER</span>
      <span class="line-sub">PACIFIC</span>
    </div>
    <div class="brand-divider"></div>
    <p class="service-tagline">Employee<br>Benefits<br>Consulting</p>

    <div class="brand-pattern" role="img" aria-label="Large decorative brand pattern in green"></div>

    <div class="contact-person">
      <h1 class="person-name">Dana Whitlow</h1>
      <p class="person-title">Principal</p>
    </div>

    <address class="postal-address">4312 Alder Crest Rd Suite C-215<br>Fernvale, WA 98172</address>

    <ul class="contact-list">
      <li>
        <svg class="contact-icon" viewBox="0 0 32 32" aria-hidden="true">
          <circle cx="16" cy="16" r="16" fill="var(--brand-green)"/>
          <rect x="8" y="10" width="16" height="12" rx="1" fill="#fff"/>
          <path d="M8.5 10.5 L16 17 L23.5 10.5" fill="none" stroke="var(--brand-green)" stroke-width="1.6"/>
        </svg>
        dana@harborledgerpac.com
      </li>
      <li>
        <svg class="contact-icon" viewBox="0 0 32 32" aria-hidden="true">
          <circle cx="16" cy="16" r="16" fill="var(--brand-green)"/>
          <rect x="10.5" y="7" width="11" height="18" rx="2" fill="#fff"/>
          <rect x="12.5" y="9.5" width="7" height="5" fill="var(--brand-green)"/>
          <g fill="var(--brand-green)">
            <rect x="12.5" y="16.5" width="2" height="2"/><rect x="15" y="16.5" width="2" height="2"/><rect x="17.5" y="16.5" width="2" height="2"/>
            <rect x="12.5" y="19.5" width="2" height="2"/><rect x="15" y="19.5" width="2" height="2"/><rect x="17.5" y="19.5" width="2" height="2"/>
          </g>
        </svg>
        425-731-4062
      </li>
    </ul>
  </section>
</body>
</html>
```